HOTEL INFORMATION

Hi, i would like to re-hire you again for the completion of our hotel information. Kindly take note of the ff:
1. attached are files of text and pictures
2. pls. feel free to choose whichever pictures suited the content
3. font is also not yet finalized thus, you may also change it
4. I also attached several pictures of the hotel that you may find useful
5. A sample picture of the compendium folder was attached for paper size adjustment (take note of the rings in the middle)
Updates
Target Market(s)
Hotel guests
Industry/Entity Type
Hotel
Look and feel
Each slider illustrates characteristics of the customer's brand and the style your logo design should communicate.

```html
<!DOCTYPE html>
<html lang="en">
<head>
<meta charset="utf-8">
<title>Amenities &amp; Services</title>
<link rel="stylesheet" href="https://fonts.googleapis.com/css2?family=Didact+Gothic&family=Josefin+Sans:wght@400&display=swap">
<style>
:root{
  --ink:#1c1c1c;
  --heading:#1e2a3a;
  --accent:#1f56c8;
  --backdrop:#000;
  --page-top:#f4f9fc;
  --page-mid:#e3f1f8;
  --page-deep:#c9e6f3;
  --rule:#5aa6e6;
}
*{margin:0;padding:0;box-sizing:border-box}
html,body{width:1200px;height:840px;overflow:hidden;background:var(--backdrop)}
.spread{position:relative;width:1200px;height:840px;background:var(--backdrop)}
.page{position:absolute;top:70px;height:712px;overflow:hidden;
  background:
    linear-gradient(135deg,rgba(255,255,255,.7) 0 30%,transparent 30% 55%,rgba(255,255,255,.45) 55% 70%,transparent 70%),
    linear-gradient(160deg,var(--page-top),var(--page-mid) 55%,var(--page-deep));}
.page--left{left:0;width:588px}
.page--right{left:612px;width:588px}
.photo{position:absolute}
.photo--pool-hero{left:0;top:0;width:588px;height:190px;
  background:linear-gradient(180deg,#7fb6d6 0%,#4aa3d9 45%,#b8dcf0 75%,rgba(228,241,248,0) 100%)}
.photo--lounge{left:0;top:556px;width:213px;height:146px;background:linear-gradient(135deg,#a0774a,#5a3c22)}
.photo--function-room{left:215px;top:556px;width:172px;height:146px;background:linear-gradient(135deg,#c9a878,#6e5030)}
.photo--restaurant{left:389px;top:556px;width:199px;height:146px;background:linear-gradient(135deg,#d8b274,#4a3320)}
.rule{position:absolute;left:0;width:588px;height:2px;background:var(--rule)}
.rule--a{top:703px}.rule--b{top:709px;height:1px}
.photo--gym{left:0;top:0;width:185px;height:143px;background:linear-gradient(135deg,#d9d9d4,#6b6b66)}
.photo--pool-deck{left:0;top:145px;width:185px;height:155px;background:linear-gradient(180deg,#4f7a46,#3f9fd8 55%,#c7a87c)}
.photo--elevators{left:0;top:303px;width:185px;height:127px;background:linear-gradient(135deg,#d6b27a,#8a6a3e)}
.photo--shop-sign{left:0;top:433px;width:185px;height:137px;background:linear-gradient(135deg,#c48c52,#5a3a20)}
.photo--towels{left:0;top:572px;width:185px;height:140px;background:linear-gradient(180deg,#b7bcc0,#f4f4f4 55%,#d7d7d7)}
.column{position:absolute;font-family:"Didact Gothic",sans-serif;color:var(--ink);font-size:9.4px;line-height:12.4px}
.column--left{left:32px;top:164px;width:528px}
.column--right{left:198px;top:104px;width:372px}
.section-title{font-family:"Josefin Sans",sans-serif;font-weight:400;font-size:17px;color:var(--heading);letter-spacing:.3px;margin-bottom:14px}
.item{margin-bottom:12px}
.item-name{font-family:"Didact Gothic",sans-serif;color:var(--accent);font-size:12.6px}
.column--right .item{margin-bottom:14px}
</style>
</head>
<body>
<div class="spread">
  <section class="page page--left">
    <div class="photo photo--pool-hero" role="img" aria-label="Resort swimming pool with lounge chairs"></div>
    <div class="column column--left">
      <h2 class="section-title">AMENITIES &amp; SERVICES</h2>
      <p class="item"><span class="item-name">Swimming Pools and Jacuzzi</span>- Surrounded by a beautifully sculpted tropical landscape, the three swimming pools at Alon Bay Resort are a heaven of serenity and tranquility. For families, the children’s pool with a water fountain is the ideal venue for fun in the sun. Be pampered by water jets in the large poolside Jacuzzi and experience the only dive pool in Alon Bay. All these are surrounded by comfortable lounge chairs and umbrellas for guest’s comfort. Pool service is available from the Restaurant café and Bar, which offer a delightful selection of thirst-quenchers and light refreshments ranging from fruit juices, soft drinks and mineral water to delightful cocktails. A good selection of wines, beers and snacks are also available for your dining pleasure.</p>
      <p class="item"><span class="item-name">Tanaw and Bituin Hall</span>- Alon Bay resort is not just a place for recreation and family bonding activities. The function rooms located at the second floor of the hotel is ideal for corporate events, business meetings/seminars, annual dinner, wedding reception and other indoor activities for a large group of people. Equipped with extensive meeting and banquet facilities, each function rooms can accommodate from 250 up to 300 pax. Our versatile function/meeting rooms are always ready. For reservations, kindly dial “0” for assistance.</p>
      <p class="item"><span class="item-name">Restaurant Café</span>- The restaurant caters to a wide range of needs from early morning breakfast to leisurely lunch and evening sumptuous dinner. We strive to provide individual services for each guest. Private dinners or cocktail parties can be arranged in a variety of locations throughout the resort to celebrate birthdays, anniversaries and other special occasions. Kindly dial “120” for assistance.</p>
      <p class="item"><span class="item-name">Bar &amp; KTV Lounge</span>- A cozy bar and lounge with an outdoor terrace overlooking the pool. Featuring live sports feeds on the big screen, light pub snacks menu, exciting cocktails and other blends. Sit down and relax to resident band’s music, dance the night away or have a private get together at the KTV lounge. Kindly dial “122” for assistance.</p>
      <p class="item"><span class="item-name">Spa</span>- No vacation is complete without a little pampering. Take time for yourself, replenish your soul and revive your tired body in our Spa. Indulge in our spa and massage services that will leave you and your muscles feeling completely rejuvenated. For additional information and to make a reservation, please dial “0”</p>
    </div>
    <div class="photo photo--lounge" role="img" aria-label="KTV lounge with sofa and screen"></div>
    <div class="photo photo--function-room" role="img" aria-label="Function hall set for a banquet"></div>
    <div class="photo photo--restaurant" role="img" aria-label="Restaurant dining room with chandeliers"></div>
    <div class="rule rule--a"></div><div class="rule rule--b"></div>
  </section>

  <section class="page page--right">
    <div class="photo photo--gym" role="img" aria-label="Fitness center with exercise machines"></div>
    <div class="photo photo--pool-deck" role="img" aria-label="Pool deck with cabana and lounge chairs"></div>
    <div class="photo photo--elevators" role="img" aria-label="Lobby elevators"></div>
    <div class="photo photo--shop-sign" role="img" aria-label="Convenience store entrance with bamboo front"></div>
    <div class="photo photo--towels" role="img" aria-label="Hands holding folded white towels"></div>
    <div class="column column--right">
      <h2 class="section-title">AMENITIES &amp; SERVICES</h2>
      <p class="item"><span class="item-name">Fitness Center</span>- Keep active and stay fit at Alon Bay Resort with exclusive fitness center access, complimentary with room reservations. Energize your body with a full array of Vitalis Fitness exercise equipment including: treadmills, cross trainer, cycling bikes, exercise ball and stretching mat.</p>
      <p class="item"><span class="item-name">Business Center</span>- A well-equipped business center is located near the lobby to facilitate processing of business plans and correspondences. The business center is equipped with state-of-the-art information technology and communication facilities that include printing, photocopying &amp; fax services and a computer system with internet access. Kindly dial “123” for assistance.</p>
      <p class="item"><span class="item-name">Kids Playground</span>- Our new, secure, outdoor playground is a great place for the kids to let off some steam. Located near the spa villas, the playground is the ideal place for the children to play in a safe environment with lots of fun to be had. Parental supervision is required.</p>
      <p class="item"><span class="item-name">Convenience Store</span>- Food, beverage, personal items and souvenirs are all available at the lobby for your convenience. Kindly dial “0” for assistance.</p>
      <p class="item"><span class="item-name">Elevator</span>- For comfort and convenience, the resort has two modern elevators available for guests</p>
      <p class="item"><span class="item-name">Housekeeping</span>- room cleaning service is offered to all guest rooms daily. Hang the “room cleaning” sign on your door knob should you require make-up room service between 8:30am to 5:30pm. Kindly dial “129” for assistance.</p>
      <p class="item"><span class="item-name">Laundry and Pressing</span>- Professional laundry, dry cleaning and clothes- pressing services are available for all guests of the resort. All laundry services are handled with the utmost care and attention. Laundry services are available daily and express service is also available. Kindly dial “129” for assistance.<br>Medical- The resort has key staff members who are certified to provide first aid should an emergency arise. A medical doctor and nurse are also available on call. Kindly dial “0” for assistance.</p>
    </div>
  </section>
</div>
</body>
</html>
```